Request for Business Card Design

Hi. My name is Marlena, I am looking for a new business card design for my company, Quillbrook Sensing Systems, LLC. I really like the design you did for Tavel Harvest and was hoping you could do something similar using our full logo and our mark. I am also open to any raised texture design using our mark. I have attached our full logo, which would need to be somewhere on the card, as well as the mark in both outline and full form, as well as our brand colors / guide. The card does not have to be white, as long as our logo and mark appear. I actually like darker colored business cards more, but am open to all options. If you are interested in working with me, please let me know. We would also take the business card design into letterhead design if you can do that.

```html
<!DOCTYPE html>
<html lang="en">
<head>
<meta charset="utf-8">
<title>Quillbrook Sensing Systems — Business Card</title>
<link rel="stylesheet" href="https://fonts.googleapis.com/css2?family=Barlow:wght@600;700&family=Nunito+Sans:wght@400;600&display=swap">
<style>
  :root {
    --stage: #1d1e23;
    --orange: #ef6f24;
    --blue: #129ac4;
    --ink: #2c3039;
    --white: #ffffff;
  }
  * { box-sizing: border-box; margin: 0; padding: 0; }
  html, body { width: 1200px; height: 800px; overflow: hidden; background: var(--stage); }
  .canvas { position: relative; width: 1200px; height: 800px; }

  .card {
    position: absolute;
    width: 525px;
    height: 300px;
    border-radius: 22px;
    overflow: hidden;
  }

  /* Front */
  .card--front { left: 70px; top: 70px; background: var(--orange); color: var(--white); }
  .front__brand {
    position: absolute; left: 0; right: 0; top: 112px;
    display: flex; align-items: center; justify-content: center; gap: 16px;
  }
  .brand-dot { width: 34px; height: 34px; border-radius: 50%; background: var(--white); flex: none; }
  .front__name {
    font-family: "Barlow", sans-serif; font-weight: 700;
    font-size: 30px; line-height: 1; letter-spacing: 1px; text-transform: uppercase;
  }
  .front__web {
    position: absolute; left: 0; right: 0; bottom: 34px; text-align: center;
    font-family: "Barlow", sans-serif; font-weight: 600; font-size: 12px; letter-spacing: 1.5px;
  }

  /* Back */
  .card--back { right: 70px; bottom: 70px; background: var(--white); color: var(--ink); }
  .back__accent { position: absolute; left: 0; top: 118px; width: 14px; height: 36px; background: var(--blue); }
  .back__mark {
    position: absolute; right: -60px; top: -70px;
    width: 260px; height: 260px; border-radius: 50%; background: var(--blue);
  }
  .back__brand {
    position: absolute; left: 40px; top: 112px;
    font-family: "Barlow", sans-serif; font-weight: 700; font-size: 26px;
    letter-spacing: 1px; text-transform: uppercase; color: var(--ink); line-height: 1.05;
  }
  .person { position: absolute; left: 40px; top: 172px; }
  .person__name {
    font-family: "Barlow", sans-serif; font-weight: 700; font-size: 19px;
    letter-spacing: .5px; text-transform: uppercase; color: var(--ink);
  }
  .person__role {
    font-family: "Barlow", sans-serif; font-weight: 600; font-size: 13px;
    letter-spacing: .5px; text-transform: uppercase; color: var(--blue); margin-top: 2px;
  }
  .contact { list-style: none; margin-top: 12px; }
  .contact__item {
    display: flex; align-items: center; gap: 8px; margin-top: 4px;
    font-family: "Nunito Sans", sans-serif; font-size: 13px; color: var(--ink);
  }
  .contact__icon { width: 16px; height: 16px; flex: none; }
</style>
</head>
<body>
<main class="canvas">

  <section class="card card--front" aria-label="Card front">
    <div class="front__brand">
      <span class="brand-dot"></span>
      <span class="front__name">Quillbrook Sensing Systems</span>
    </div>
    <p class="front__web">WWW.QUILLBROOKSENSING.COM</p>
  </section>

  <section class="card card--back" aria-label="Card back">
    <div class="back__mark"></div>
    <div class="back__accent"></div>
    <p class="back__brand">Quillbrook<br>Sensing Systems</p>
    <div class="person">
      <p class="person__name">Marlena Vance</p>
      <p class="person__role">Managing Director</p>
      <ul class="contact">
        <li class="contact__item">
          <svg class="contact__icon" viewBox="0 0 16 16"><circle cx="8" cy="8" r="7.3" fill="none" stroke="#129ac4" stroke-width="1.2"/><path d="M5.4 4.6l1.3-.3.7 1.7-.8.7a4.6 4.6 0 0 0 2.5 2.5l.7-.8 1.7.7-.3 1.3c-3.3.2-6-2.5-5.8-5.8z" fill="#129ac4"/></svg>
          555-018-2744
        </li>
        <li class="contact__item">
          <svg class="contact__icon" viewBox="0 0 16 16"><circle cx="8" cy="8" r="7.3" fill="none" stroke="#129ac4" stroke-width="1.2"/><rect x="4.3" y="5.4" width="7.4" height="5.2" fill="none" stroke="#129ac4" stroke-width="1"/><path d="M4.3 5.4L8 8.4l3.7-3" fill="none" stroke="#129ac4" stroke-width="1"/></svg>
          marlena@quillbrooksensing.com
        </li>
        <li class="contact__item">
          <svg class="contact__icon" viewBox="0 0 16 16"><circle cx="8" cy="8" r="7.3" fill="none" stroke="#129ac4" stroke-width="1.2"/><circle cx="8" cy="8" r="4" fill="none" stroke="#129ac4" stroke-width="1"/><ellipse cx="8" cy="8" rx="1.7" ry="4" fill="none" stroke="#129ac4" stroke-width="1"/><path d="M4 8h8" stroke="#129ac4" stroke-width="1"/></svg>
          www.quillbrooksensing.com
        </li>
      </ul>
    </div>
  </section>

</main>
</body>
</html>
```